Young Pilgrims-2017

a Spiritual journey for the years to follow

Package Includes :
- Under Guidance of a Sheikh
- 5 Star Accommodation in Medina & Makkah
- 4 - 5 Person Sharing
- 20 - 22 Days Trip
- Post and Pre Lectures
- Age Group 18+ Years
- For Brothers & Families

With Rehan Jameel Farooqui
& Brother Bilal Qureshi

Contact :
Bilal Qureshi +92 333 5810462
bilalqureshi@[url removed, login to view]

```html
<!DOCTYPE html>
<html lang="en">
<head>
<meta charset="utf-8">
<title>Young Pilgrims 2017 Flyer</title>
<link href="https://fonts.googleapis.com/css2?family=Philosopher:wght@400;700&family=Libre+Baskerville:ital,wght@0,400;0,700;1,700&display=swap" rel="stylesheet">
<style>
  :root {
    --stage: #e9eaec;
    --paper: #dff3f4;
    --paper-edge: #c8e8ea;
    --ocean: #1f6f97;
    --ocean-deep: #0f4f75;
    --ocean-light: #8fd2e6;
    --gold: #e7c21d;
    --gold-deep: #b9940a;
    --ink: #1c2b33;
    --white: #ffffff;
  }
  * { box-sizing: border-box; margin: 0; padding: 0; }
  html, body { width: 1200px; height: 675px; overflow: hidden; }
  body {
    background: var(--stage);
    font-family: "Libre Baskerville", Georgia, serif;
    color: var(--ink);
    position: relative;
  }
  .flyer {
    position: absolute;
    left: 370px; top: 18px;
    width: 460px; height: 640px;
    background: radial-gradient(ellipse at 50% 35%, var(--paper) 40%, var(--paper-edge) 100%);
    overflow: hidden;
  }
  .title-ribbon {
    position: absolute; left: 0; right: 0; top: 24px; height: 52px;
    background: linear-gradient(90deg, rgba(31,111,151,0) 0%, var(--ocean) 18%, var(--ocean-light) 55%, var(--ocean) 85%, rgba(31,111,151,0) 100%);
    display: flex; align-items: center; justify-content: center;
  }
  .title {
    font-family: "Philosopher", "Trebuchet MS", sans-serif;
    font-weight: 700; font-size: 31px; color: var(--white);
    letter-spacing: 0.5px;
  }
  .tagline {
    position: absolute; top: 96px; left: 0; right: 0;
    text-align: center; font-weight: 700; font-size: 13.5px;
  }
  .gold-rule {
    position: absolute; left: 18px; right: 18px; height: 2px;
    background: linear-gradient(90deg, transparent, var(--gold) 15%, var(--gold) 85%, transparent);
  }
  .rule-top { top: 140px; }
  .rule-bottom { top: 268px; }
  .package-label {
    position: absolute; top: 131px; left: 50%; transform: translateX(-50%);
    padding: 3px 16px;
    background: linear-gradient(180deg, #f6dd5a, var(--gold-deep));
    border-radius: 10px;
    font-size: 10px; font-weight: 700; color: var(--ocean-deep);
    white-space: nowrap;
  }
  .package-list {
    position: absolute; top: 164px; left: 40px; right: 30px;
    display: grid; grid-template-columns: 1.15fr 1fr; column-gap: 14px;
    list-style: none;
  }
  .package-list .col { display: flex; flex-direction: column; gap: 9px; }
  .package-list li {
    display: flex; align-items: flex-start; gap: 8px;
    font-size: 8px; font-weight: 700; line-height: 1.35;
  }
  .bullet {
    flex: none; width: 11px; height: 11px; border-radius: 50%;
    background: radial-gradient(circle, var(--white) 30%, var(--gold) 32%, var(--gold-deep) 100%);
  }
  .hosts {
    position: absolute; top: 294px; left: 0; right: 0;
    text-align: center; color: var(--ocean-deep);
    font-weight: 700; font-size: 12.5px; line-height: 1.35;
  }
  .hosts em { font-size: 15px; display: block; }
  .kaaba-scene {
    position: absolute; left: 0; right: 0; top: 340px; height: 210px;
    background: linear-gradient(180deg, rgba(255,255,255,0) 0%, #f2f6f7 35%, #d6dde0 100%);
  }
  .footer-band { position: absolute; left: 0; bottom: 0; width: 460px; height: 120px; }
  .contact-name {
    position: absolute; bottom: 82px; left: 0; right: 0;
    text-align: center; color: var(--white); font-weight: 700; font-size: 11px;
  }
  .contact-row {
    position: absolute; bottom: 26px; left: 18px; right: 18px;
    display: flex; justify-content: space-between;
    color: var(--white); font-size: 8.5px; font-weight: 700;
  }
  .contact-row span { display: flex; align-items: center; gap: 5px; }
  .icon-dot {
    width: 16px; height: 16px; border-radius: 50%;
    border: 1.5px solid var(--white);
    display: inline-flex; align-items: center; justify-content: center;
  }
</style>
</head>
<body>
  <article class="flyer">
    <div class="title-ribbon"><h1 class="title">Young Pilgrims 2017</h1></div>
    <p class="tagline">A Spiritual journey for the years to follow</p>

    <div class="gold-rule rule-top"></div>
    <div class="package-label">Package Includes :</div>
    <ul class="package-list">
      <div class="col">
        <li><span class="bullet"></span>Under Guidance of a Sheikh</li>
        <li><span class="bullet"></span>5 Star Accommodation in<br>Medina &amp; Makkah</li>
        <li><span class="bullet"></span>4 - 5 Person Sharing</li>
        <li><span class="bullet"></span>20 - 22 Days Trip</li>
      </div>
      <div class="col">
        <li><span class="bullet"></span>Post and Pre Lectures</li>
        <li><span class="bullet"></span>Age Group 18+ Years</li>
        <li><span class="bullet"></span>For Brothers &amp; Families</li>
      </div>
    </ul>
    <div class="gold-rule rule-bottom"></div>

    <p class="hosts"><em>With</em>Rehan Jameel Farooqui<br>&amp; Brother Bilal Qureshi</p>

    <div class="kaaba-scene" role="img" aria-label="Illustration of the Kaaba with gold band between two white minarets and arcade"></div>

    <svg class="footer-band" viewBox="0 0 460 120" aria-hidden="true">
      <defs>
        <linearGradient id="bandFill" x1="0" y1="0" x2="0" y2="1">
          <stop offset="0" stop-color="#2b84ac"/>
          <stop offset="1" stop-color="#0f4f75"/>
        </linearGradient>
      </defs>
      <path d="M0 30 Q230 -10 460 30 L460 120 L0 120 Z" fill="var(--gold)"/>
      <path d="M0 34 Q230 -4 460 34 L460 120 L0 120 Z" fill="url(#bandFill)"/>
    </svg>
    <p class="contact-name">Contact: Bilal Qureshi</p>
    <div class="contact-row">
      <span><i class="icon-dot"><svg width="8" height="8" viewBox="0 0 10 10"><path d="M2 1 L4 1 L4.5 3 L3.3 4 Q4.5 6 6 6.7 L7 5.5 L9 6 L9 8 Q4 9 1 2 Z" fill="#fff"/></svg></i>+92 333 5810462</span>
      <span><i class="icon-dot"><svg width="9" height="7" viewBox="0 0 10 8"><rect x="0.5" y="0.5" width="9" height="7" fill="none" stroke="#fff"/><path d="M0.5 0.5 L5 4.5 L9.5 0.5" fill="none" stroke="#fff"/></svg></i>bilalqureshi@pilgrimmail.com</span>
      <span><i class="icon-dot"></i>pilgrimsyouth.page</span>
    </div>
  </article>
</body>
</html>
```